tallkettle.example - youth/backpackers Adventure Travel contact site

Landing Page: Logo, @RidgelineRoamerCrew, Australia | New Zealand | Fiji | South East Asia, Start Button, a Rotating carousel of supplier logos, ©Tall Kettle Travel, Terms and Conditions link, Contact Us page link, social media/contact icons.
Start Button: Takes you to destinations selection Map - Hover over effect with selectable Countries, states, regions, and next & back buttons.
Next Button: Takes you to Activities - Selectable Buttons for Sky Diving, Sailing, Whitewater Rafting, Bungee jumping, camping, hiking, Surfing, Jet Boating, kayaking, canyoning, National Parks, Scuba Diving, Snorkeling and beaches etc., Tandem Hand gliding, with a typable "Have we missed anything you want to experience" area and back and next buttons.
Next Button: Takes you to extras - Selectable buttons for Bus Passes, Accommodation, Car Hire, Camper Hire and back and next buttons.
Next Button: Takes you to enter customer details: Name, Age, Phone, Email, How did you hear about us, Dietary requirement, start & end date, start & end location, Number of Travellers, Budget, anything else area, Submit for your custom adventure button. - All this information then gets emailed.

Target Market(s)

Backpacker/youth adventure travel

Industry/Entity Type

Travel Agent

Coding

Coded - Design and coding required

Number of Pages Required

3 page

Colors

Designer to choose colors to be used in the design.

Requirements
Must have
• Somewhere to be automatically synced Instagram profile pictures and videos.
• Full screen, scalable to any device size - 65% of our users use mobile devices.
• Wordpress
Nice to have
• Easy to add and remove selectable buttons
• If you can think of any special feature to add ;)
Should not have
• Basic contact form look

```html
<!DOCTYPE html>
<html lang="en">
<head>
<meta charset="utf-8">
<title>Tall Kettle Travel — Adventure Travel Specialists</title>
<link rel="stylesheet" href="https://fonts.googleapis.com/css2?family=Lora:ital,wght@0,400;0,700;1,400;1,700&display=swap">
<style>
  :root {
    --sky-glow: #fbf3c8;
    --hill-light: #b7c46a;
    --hill-mid: #7f9a3e;
    --hill-deep: #4f6a2c;
    --valley-teal: #6f9a86;
    --grass-gold: #b49a4a;
    --text-light: #ffffff;
    --accent-red: #f25a4e;
    --tile-bg: rgba(236, 236, 236, 0.82);
    --tile-ink: #555555;
    --rule: rgba(255, 255, 255, 0.8);
    --social-blue: #3b63c4;
    --social-red: #c3343c;
    --social-pink: #d8376f;
    --social-sky: #1f8be0;
  }
  * { box-sizing: border-box; margin: 0; padding: 0; }
  html, body { width: 1200px; height: 755px; overflow: hidden; }
  body { font-family: "Lora", Georgia, serif; color: var(--text-light); }

  .landing { position: relative; width: 1200px; height: 755px; overflow: hidden; }

  .hero-photo {
    position: absolute; inset: 0;
    background:
      radial-gradient(ellipse 520px 360px at 1120px 90px, var(--sky-glow) 0%, rgba(251,243,200,0) 70%),
      linear-gradient(180deg, var(--valley-teal) 0%, var(--hill-light) 30%, var(--hill-mid) 52%, var(--hill-deep) 70%, var(--grass-gold) 88%, #8c7a3a 100%);
  }

  .brand {
    position: absolute; top: 62px; left: 0; width: 100%;
    display: flex; justify-content: center; align-items: center; gap: 10px;
  }
  .brand-dot { width: 22px; height: 22px; border-radius: 50%; background: var(--accent-red); }
  .brand-name { font-weight: 700; font-size: 26px; color: var(--accent-red); }

  .headline {
    position: absolute; top: 198px; width: 100%; text-align: center;
    font-size: 39px; font-weight: 700; letter-spacing: 0.5px;
    text-shadow: 0 1px 4px rgba(0,0,0,0.25);
  }
  .tagline {
    position: absolute; top: 264px; width: 100%; text-align: center;
    font-size: 18px;
  }
  .destinations {
    position: absolute; top: 305px; width: 100%; text-align: center;
    font-size: 13px; font-style: italic; font-weight: 700; word-spacing: 2px;
  }
  .destinations .sep { margin: 0 9px; font-style: normal; }

  .start-button {
    position: absolute; top: 353px; left: 538px; width: 124px; height: 33px;
    border-radius: 17px; background: var(--accent-red); color: var(--text-light);
    font-size: 14px; font-weight: 400; letter-spacing: 0.5px;
    display: flex; align-items: center; justify-content: center; gap: 8px;
    text-decoration: none;
  }

  .supplier-carousel { position: absolute; top: 435px; left: 0; width: 100%; height: 80px; }
  .carousel-arrow { position: absolute; top: 22px; width: 20px; height: 34px; }
  .carousel-arrow.prev { left: 42px; }
  .carousel-arrow.next { left: 1132px; }
  .supplier-tile {
    position: absolute; top: 0; width: 155px; height: 79px;
    background: var(--tile-bg); color: var(--tile-ink);
    display: flex; flex-direction: column; align-items: center; justify-content: center; gap: 4px;
    text-align: center;
  }
  .supplier-name { font-size: 12px; font-weight: 700; letter-spacing: 0.5px; }
  .supplier-line { font-size: 6px; letter-spacing: 3px; }

  .footer-rule { position: absolute; top: 679px; left: 99px; width: 1002px; height: 1px; background: var(--rule); }
  .footer-links {
    position: absolute; top: 710px; left: 99px; font-size: 13px;
    display: flex; gap: 14px; align-items: center;
  }
  .footer-links a { color: var(--text-light); text-decoration: none; }
  .social { position: absolute; top: 699px; left: 910px; display: flex; gap: 16px; }
  .social-link {
    width: 36px; height: 36px; border-radius: 50%;
    display: flex; align-items: center; justify-content: center;
  }
  .social-link.one { background: var(--social-blue); }
  .social-link.two { background: var(--social-red); }
  .social-link.three { background: var(--social-pink); }
  .social-link.mail { background: var(--social-sky); }
</style>
</head>
<body>
<main class="landing">
  <div class="hero-photo" role="img" aria-label="Photo of a backpacker looking over sunlit green mountain valleys and golden grass"></div>

  <div class="brand">
    <span class="brand-dot"></span>
    <span class="brand-name">Tall Kettle Travel</span>
  </div>

  <h1 class="headline">Tall Kettle Travel</h1>
  <p class="tagline">Adventure Travel Specialists</p>
  <p class="destinations">Australia<span class="sep">|</span>New Zealand<span class="sep">|</span>Fiji<span class="sep">|</span>South East Asia</p>

  <a class="start-button" href="#destinations">START NOW
    <svg width="6" height="8" viewBox="0 0 6 8"><path d="M0 0L6 4L0 8Z" fill="#fff"/></svg>
  </a>

  <section class="supplier-carousel" aria-label="Our suppliers">
    <svg class="carousel-arrow prev" viewBox="0 0 20 34"><path d="M16 4L4 17L16 30" fill="none" stroke="#fff" stroke-width="3.5"/></svg>
    <div class="supplier-tile" style="left:99px"><span class="supplier-name">COMPANY NAME</span><span class="supplier-line">SLOGAN</span></div>
    <div class="supplier-tile" style="left:268px"><span class="supplier-name">COMPANY NAME</span><span class="supplier-line">SLOGAN</span></div>
    <div class="supplier-tile" style="left:438px"><span class="supplier-name">COMPANY NAME</span></div>
    <div class="supplier-tile" style="left:607px"><span class="supplier-name">COMPANY NAME</span><span class="supplier-line">SLOGAN</span></div>
    <div class="supplier-tile" style="left:777px"><span class="supplier-name">Brightfold Link</span><span class="supplier-line" style="letter-spacing:0.5px">your tagline here</span></div>
    <div class="supplier-tile" style="left:946px"><span class="supplier-name">COMPANY</span><span class="supplier-line">YOUR SLOGAN</span></div>
    <svg class="carousel-arrow next" viewBox="0 0 20 34"><path d="M4 4L16 17L4 30" fill="none" stroke="#fff" stroke-width="3.5"/></svg>
  </section>

  <div class="footer-rule"></div>
  <footer class="footer-links">
    <span>©2017 Tall Kettle Travel</span><span>|</span>
    <a href="#terms">Terms and Conditions</a><span>|</span>
    <a href="#contact">Contact Us</a>
  </footer>
  <nav class="social" aria-label="Social and contact">
    <a class="social-link one" href="#" aria-label="Social profile"></a>
    <a class="social-link two" href="#" aria-label="Video channel"></a>
    <a class="social-link three" href="#" aria-label="Photo feed"></a>
    <a class="social-link mail" href="#contact" aria-label="Email us">
      <svg width="15" height="11" viewBox="0 0 15 11"><rect x="0" y="0" width="15" height="11" rx="1.5" fill="#fff"/><path d="M0.5 1L7.5 6L14.5 1" fill="none" stroke="#1f8be0" stroke-width="1.4"/></svg>
    </a>
  </nav>
</main>
</body>
</html>
```